VORTEQ

It’s is a startup business. We design and build new products.

Target Market(s)

For my first two products, they are targeting the laundry market, hanger accessory, and new modern style clothes dryer. I also have a Pet Treat product at patent stage, and there are other products not yet started but will be more engineering based. Therefore from young adults to older population

Industry/Entity Type

Colours of website to match the logo (att)

Coding

Coded - Design and coding required

Number of Pages Required

1 page

Font styles to use
Other font styles liked:
• Some of the same font as the logo

Colors

Designer to choose colors to be used in the design.

Requirements
Must have
• An upbeat vibe - the logo looks great so inline with that !
Should not have
• anything old fashioned and old style fonts

```html
<!DOCTYPE html>
<html lang="en">
<head>
<meta charset="utf-8">
<title>VORTEQ — Innovation Technical Services</title>
<link href="https://fonts.googleapis.com/css2?family=Michroma&family=Lato:wght@400;700&display=swap" rel="stylesheet">
<style>
:root{
  --teal:#00c6c6;
  --teal-soft:#6fd9d9;
  --cyan:#13b6e0;
  --navy:#2b3183;
  --ink:#1c1c1c;
  --text:#3a3a3a;
  --hero-dark:#0a2340;
  --hero-mid:#1b5a8a;
  --why-bg:#e8e7e3;
  --ring:#3d4650;
  --footer:#3a3a3c;
  --star:#f2c200;
  --white:#ffffff;
}
*{margin:0;padding:0;box-sizing:border-box}
html,body{width:1200px;height:3687px;overflow:hidden}
body{position:relative;background:var(--white);font-family:"Lato",sans-serif;color:var(--text)}
.display{font-family:"Michroma",sans-serif;text-transform:uppercase;color:var(--ink)}
.abs{position:absolute}

/* header */
.site-header{position:absolute;left:0;top:0;width:1200px;height:86px;background:var(--white)}
.brand{position:absolute;left:112px;top:26px;display:flex;align-items:center;gap:10px}
.brand-dot{width:28px;height:28px;border-radius:50%;background:var(--teal)}
.brand-name{font-family:"Michroma",sans-serif;font-size:24px;color:var(--navy);letter-spacing:2px}
.main-nav{position:absolute;left:426px;top:33px;display:flex;gap:22px}
.main-nav a{font-family:"Michroma",sans-serif;font-size:12px;letter-spacing:2px;color:var(--ink);text-decoration:none;text-transform:uppercase}
.nav-contact{position:absolute;left:955px;top:20px;width:133px;height:45px;background:var(--navy);border-radius:3px;color:var(--white);font-family:"Michroma",sans-serif;font-size:12px;letter-spacing:2px;display:flex;align-items:center;justify-content:center;text-transform:uppercase}

/* hero */
.hero{position:absolute;left:0;top:86px;width:1200px;height:614px}
.hero-photo{position:absolute;inset:0;background:radial-gradient(circle at 78% 25%,#c9a46a 0,#3b6f9a 12%,transparent 30%),linear-gradient(120deg,var(--hero-dark) 0%,var(--hero-mid) 55%,#0d2c4d 100%)}
.hero-shape{position:absolute;left:0;top:0}
.hero-title{position:absolute;left:112px;top:130px;font-family:"Michroma",sans-serif;font-size:44px;letter-spacing:6px;color:var(--white)}
.hero-sub{position:absolute;left:112px;top:195px;font-size:19px;font-weight:700;color:var(--white);letter-spacing:.5px}
.hero-text{position:absolute;left:112px;top:231px;width:420px;font-size:15.5px;line-height:28px;color:#e6eef6}
.btn{position:absolute;display:flex;align-items:center;justify-content:center;font-family:"Michroma",sans-serif;font-size:12px;letter-spacing:2px;color:var(--white);text-transform:uppercase;border-radius:2px}
.hero-btn{left:112px;top:304px;width:191px;height:44px;background:var(--teal)}

/* about */
.about-frame-navy{position:absolute;left:126px;top:782px;width:172px;height:140px;border-left:10px solid var(--navy);border-top:10px solid var(--navy)}
.about-frame-teal{position:absolute;left:393px;top:1012px;width:172px;height:139px;border-right:7px solid var(--teal);border-bottom:7px solid var(--teal)}
.about-photo{position:absolute;left:143px;top:799px;width:408px;height:338px;background:linear-gradient(135deg,#2f6aa0 0%,#6fa2c8 45%,#1f3f66 100%)}
.section-heading{font-family:"Michroma",sans-serif;text-transform:uppercase;color:var(--ink);font-size:24px;letter-spacing:5px}
.heading-rule{position:absolute;height:4px;background:var(--teal)}
.about-heading{position:absolute;left:620px;top:792px}
.about-copy{position:absolute;left:620px;top:862px;width:460px;font-size:14.5px;line-height:25.7px;color:var(--text)}
.about-copy p+p{margin-top:25px}
.about-btn{left:620px;top:1088px;width:164px;height:45px;background:linear-gradient(90deg,var(--teal),var(--navy))}

/* services */
.services-band{position:absolute;left:0;top:1254px;width:1200px;height:491px;background:linear-gradient(90deg,var(--teal) 0%,#1a8fc0 55%,var(--navy) 100%)}
.center-heading{position:absolute;left:0;width:1200px;text-align:center}
.service-photo{position:absolute;top:1434px;width:436px;height:311px}
.service-title{position:absolute;top:1774px;width:436px;text-align:center;font-family:"Michroma",sans-serif;font-size:16px;letter-spacing:3px;color:var(--ink);text-transform:uppercase}
.service-text{position:absolute;top:1807px;width:400px;text-align:center;font-size:14.5px;line-height:25.7px;color:var(--text)}

/* why */
.why{position:absolute;left:0;top:2035px;width:1200px;height:644px;background:var(--why-bg)}
.why-item{position:absolute;width:240px;font-size:15px;line-height:28px;color:var(--text)}
.why-item h3{font-size:16px;font-weight:700;color:var(--ink);margin-bottom:4px}
.why-left{text-align:right}

/* testimonials */
.testimonial-card{position:absolute;top:2907px;width:308px;height:189px;background:var(--white);border-radius:14px;box-shadow:0 8px 18px rgba(0,0,0,.09)}
.card-top{position:absolute;top:2907px;height:3px;background:var(--navy);border-radius:3px}
.card-pointer{position:absolute;top:3092px;width:0;height:0;border-left:9px solid transparent;border-right:9px solid transparent;border-top:9px solid var(--white)}
.avatar{position:absolute;top:2862px;width:90px;height:90px;border-radius:50%;background:linear-gradient(160deg,#d9c2ae,#8a8f98);border:3px solid var(--white)}
.testimonial-text{position:absolute;top:2983px;width:270px;text-align:center;font-size:14.5px;line-height:25.7px;color:var(--text)}
.reviewer{position:absolute;top:3124px;width:308px;text-align:center;font-size:14.5px;color:var(--ink)}
.reviewer .stars{color:var(--star);letter-spacing:1px;margin-left:18px;font-size:14px}

/* footer */
.site-footer{position:absolute;left:0;top:3239px;width:1200px;height:448px;background:var(--footer);color:var(--white)}
.footer-heading{position:absolute;top:68px;font-size:21px;font-weight:700;letter-spacing:.3px}
.quick-links{position:absolute;left:97px;top:107px;list-style:none}
.quick-links li{font-size:15px;height:31px;display:flex;align-items:center;gap:10px}
.footer-divider{position:absolute;top:89px;width:1px;height:238px;background:#8a8a8c}
.social{position:absolute;left:97px;top:317px;display:flex;gap:5px}
.social span{width:32px;height:32px;border:1.5px solid var(--white);border-radius:50%}
.contact-item{position:absolute;left:355px;width:240px}
.contact-icon{position:absolute;left:0;top:2px;width:32px;height:32px;border-radius:50%;background:var(--teal);display:flex;align-items:center;justify-content:center}
.contact-item h4{margin-left:45px;font-size:17px;font-weight:700}
.contact-item p{margin-left:45px;font-size:15.5px;margin-top:8px}
.contact-rule{position:absolute;left:355px;width:240px;border-top:1px dashed #9a9a9c}
.field{position:absolute;left:715px;width:353px;height:40px;border:1px solid #bdbdbd;border-radius:2px;font-size:15px;padding:0 13px;display:flex;align-items:center}
.submit{position:absolute;left:715px;top:261px;width:353px;height:38px;background:var(--teal);border-radius:2px;font-size:17px;font-weight:700;display:flex;align-items:center;justify-content:center}
.footer-bottom-rule{position:absolute;left:97px;top:388px;width:1003px;height:1px;background:#8a8a8c}
.copyright{position:absolute;left:0;top:406px;width:1200px;text-align:center;font-size:15.5px}
</style>
</head>
<body>

<header class="site-header">
  <div class="brand"><span class="brand-dot"></span><span class="brand-name">VORTEQ</span></div>
  <nav class="main-nav"><a>Home</a><a>About Us</a><a>Services</a><a>Products</a></nav>
  <div class="nav-contact">Contact</div>
</header>

<section class="hero">
  <div class="hero-photo" role="img" aria-label="Robotic hand and human hand reaching toward a glowing light bulb over a blue circuit backdrop"></div>
  <svg class="hero-shape" width="1200" height="614" viewBox="0 0 1200 614">
    <defs>
      <linearGradient id="heroBand" x1="0" x2="1" y1="0" y2="0">
        <stop offset="0" stop-color="#00c6c6"/>
        <stop offset="0.5" stop-color="#1aa3c4"/>
        <stop offset="1" stop-color="#2b3183"/>
      </linearGradient>
    </defs>
    <polygon points="0,469 598,572 1200,486 1200,614 0,614" fill="#ffffff"/>
    <polygon points="122,505 598,595 1173,490 598,614" fill="url(#heroBand)"/>
  </svg>
  <h1 class="hero-title">VORTEQ</h1>
  <p class="hero-sub">INNOVATION TECHNICAL SERVICES</p>
  <p class="hero-text">Excepteur sint occaecat cupidatat non proident, sunt in culpa qui officia deserunt mollit anim id est laborum.</p>
  <div class="btn hero-btn">Get Started</div>
</section>

<section class="about">
  <div class="about-frame-navy"></div>
  <div class="about-frame-teal"></div>
  <div class="about-photo" role="img" aria-label="Two engineers reviewing a tablet in a modern workshop"></div>
  <h2 class="section-heading about-heading">About Us</h2>
  <div class="heading-rule" style="left:620px;top:841px;width:63px"></div>
  <div class="about-copy">
    <p>Lorem ipsum dolor sit amet, consectetur adipiscing elit, sed do eiusmod tempor incididunt ut labore et dolore magna aliqua. Ut enim ad minim veniam, quis nostrud exercitation ullamco laboris nisi ut aliquip ex ea commodo consequat.</p>
    <p>Duis aute irure dolor in reprehenderit in voluptate velit esse cillum dolore eu fugiat nulla pariatur. Excepteur sint occaecat cupidatat non proident, sunt in culpa qui officia deserunt mollitlaborum.</p>
  </div>
  <div class="btn about-btn">Read More</div>
</section>

<section class="services">
  <div class="services-band"></div>
  <h2 class="section-heading center-heading" style="top:1340px;color:var(--white)">Our Services</h2>
  <div class="heading-rule" style="left:570px;top:1387px;width:60px;background:var(--white)"></div>
  <div class="service-photo" style="left:137px;background:linear-gradient(120deg,#e9ecef,#b9c0c7 60%,#d8dde1)" role="img" aria-label="Row of front-loading washing machines in a laundromat"></div>
  <div class="service-photo" style="left:626px;background:linear-gradient(135deg,#6e4a2c,#b07a4a 50%,#4a3020)" role="img" aria-label="Puppy eating from a bowl of pet treats"></div>
  <h3 class="service-title" style="left:137px">Laundry Market</h3>
  <h3 class="service-title" style="left:626px">Pet Treat</h3>
  <p class="service-text" style="left:155px">Lorem ipsum dolor sit amet, consectetur adipiscing elit, sed do eiusmod tempor incididunt ut labore et dolore magna aliqua.</p>
  <p class="service-text" style="left:644px">Lorem ipsum dolor sit amet, consectetur adipiscing elit, sed do eiusmod tempor incididunt ut labore et dolore magna aliqua.</p>
  <div class="btn" style="left:274px;top:1900px;width:163px;height:45px;background:var(--navy)">Read More</div>
  <div class="btn" style="left:763px;top:1900px;width:163px;height:45px;background:var(--teal)">Read More</div>
</section>

<section class="why">
  <h2 class="section-heading center-heading" style="top:95px">Why Choose Us</h2>
  <div class="heading-rule" style="left:561px;top:143px;width:78px"></div>
  <svg class="abs" style="left:0;top:0" width="1200" height="644" viewBox="0 0 1200 644">
    <g fill="none" stroke="#3d4650" stroke-width="1.5">
      <polyline points="421,206 482,206 517,243"/>
      <polyline points="743,206 690,206 654,243"/>
      <polyline points="421,424 475,424 508,389"/>
      <polyline points="743,424 696,424 663,389"/>
    </g>
    <circle cx="586" cy="325" r="98" fill="#ffffff" stroke="#3d4650" stroke-width="13"/>
    <text x="586" y="333" text-anchor="middle" font-family="Lato, sans-serif" font-weight="700" font-size="24" fill="#2b3183">VORTEQ</text>
    <circle cx="385" cy="206" r="36" fill="#00c6c6"/>
    <circle cx="778" cy="205" r="36" fill="#2b3183"/>
    <circle cx="385" cy="408" r="36" fill="#6fd9d9"/>
    <circle cx="778" cy="408" r="36" fill="#13b6e0"/>
    <g fill="none" stroke="#ffffff" stroke-width="3" stroke-linecap="round" stroke-linejoin="round">
      <path d="M370 218h30M376 218v-14h18v14M385 204v-10l8 4-8 4"/>
      <path d="M770 220h18M776 220c0-8 4-12 4-24M780 196l10 5-10 5"/>
      <path d="M372 420v-22h12v22M384 420v-14h12v14M370 420h30"/>
      <circle cx="778" cy="408" r="9"/>
      <path d="M778 390v6M778 420v6M760 408h6M790 408h6M765 395l4 4M791 421l-4-4M791 395l-4 4M765 421l4-4"/>
    </g>
  </svg>
  <div class="why-item why-left" style="left:182px;top:257px"><h3>Excepteur sint occaecat</h3>Lorem ipsum dolor sit amet,<br>consectetur adipiscing</div>
  <div class="why-item" style="left:742px;top:258px"><h3>Excepteur sint occaecat</h3>Lorem ipsum dolor sit amet,<br>consectetur adipiscing</div>
  <div class="why-item why-left" style="left:182px;top:459px"><h3>Excepteur sint occaecat</h3>Lorem ipsum dolor sit amet,<br>consectetur adipiscing</div>
  <div class="why-item" style="left:742px;top:460px"><h3>Excepteur sint occaecat</h3>Lorem ipsum dolor sit amet,<br>consectetur adipiscing</div>
</section>

<section class="testimonials">
  <h2 class="section-heading center-heading" style="top:2768px">Testimonials</h2>
  <div class="heading-rule" style="left:561px;top:2816px;width:78px"></div>

  <div class="testimonial-card" style="left:112px"></div>
  <div class="card-top" style="left:112px;width:100px"></div><div class="card-top" style="left:320px;width:100px"></div>
  <div class="card-pointer" style="left:257px"></div>
  <div class="avatar" style="left:220px" role="img" aria-label="Customer portrait"></div>
  <p class="testimonial-text" style="left:131px">Sed ut perspiciatis unde omnis iste natus error sit voluptatem accusantium doloremque laudantium, totam rem aperiam, eaque ipsa</p>
  <div class="reviewer" style="left:112px">Maya Lorne<span class="stars">★★★★★</span></div>

  <div class="testimonial-card" style="left:445px"></div>
  <div class="card-top" style="left:445px;width:100px"></div><div class="card-top" style="left:653px;width:100px"></div>
  <div class="card-pointer" style="left:590px"></div>
  <div class="avatar" style="left:553px" role="img" aria-label="Customer portrait"></div>
  <p class="testimonial-text" style="left:464px">Sed ut perspiciatis unde omnis iste natus error sit voluptatem accusantium doloremque laudantium, totam rem aperiam, eaque ipsa</p>
  <div class="reviewer" style="left:445px">Maya Lorne<span class="stars">★★★★★</span></div>

  <div class="testimonial-card" style="left:778px"></div>
  <div class="card-top" style="left:778px;width:100px"></div><div class="card-top" style="left:986px;width:100px"></div>
  <div class="card-pointer" style="left:923px"></div>
  <div class="avatar" style="left:886px" role="img" aria-label="Customer portrait"></div>
  <p class="testimonial-text" style="left:797px">Sed ut perspiciatis unde omnis iste natus error sit voluptatem accusantium doloremque laudantium, totam rem aperiam, eaque ipsa</p>
  <div class="reviewer" style="left:778px">Maya Lorne<span class="stars">★★★★★</span></div>
</section>

<footer class="site-footer">
  <h3 class="footer-heading" style="left:97px">QUICK LINKS</h3>
  <ul class="quick-links">
    <li><svg width="14" height="12" viewBox="0 0 14 12"><path d="M1 6h11M7 1l5 5-5 5" stroke="#fff" stroke-width="2.4" fill="none"/></svg>Home</li>
    <li><svg width="14" height="12" viewBox="0 0 14 12"><path d="M1 6h11M7 1l5 5-5 5" stroke="#fff" stroke-width="2.4" fill="none"/></svg>About Vorteq</li>
    <li><svg width="14" height="12" viewBox="0 0 14 12"><path d="M1 6h11M7 1l5 5-5 5" stroke="#fff" stroke-width="2.4" fill="none"/></svg>Product</li>
    <li><svg width="14" height="12" viewBox="0 0 14 12"><path d="M1 6h11M7 1l5 5-5 5" stroke="#fff" stroke-width="2.4" fill="none"/></svg>Industries We Serve</li>
    <li><svg width="14" height="12" viewBox="0 0 14 12"><path d="M1 6h11M7 1l5 5-5 5" stroke="#fff" stroke-width="2.4" fill="none"/></svg>Resources</li>
    <li><svg width="14" height="12" viewBox="0 0 14 12"><path d="M1 6h11M7 1l5 5-5 5" stroke="#fff" stroke-width="2.4" fill="none"/></svg>Contact</li>
  </ul>
  <div class="social"><span></span><span></span><span></span><span></span></div>
  <div class="footer-divider" style="left:302px"></div>

  <h3 class="footer-heading" style="left:355px">CONTACT DETAILS</h3>
  <div class="contact-item" style="top:108px">
    <div class="contact-icon"><svg width="16" height="16" viewBox="0 0 16 16"><path d="M3 1l3 3-2 2c1 2 3 4 5 5l2-2 3 3-2 3C7 15 1 9 0 3z" fill="#fff"/></svg></div>
    <h4>Phone:</h4><p>+1 555 0142 7788</p>
  </div>
  <div class="contact-rule" style="top:170px"></div>
  <div class="contact-item" style="top:189px">
    <div class="contact-icon"><svg width="16" height="12" viewBox="0 0 16 12"><rect x="0" y="0" width="16" height="12" rx="1" fill="#fff"/><path d="M0 1l8 6 8-6" stroke="#00c6c6" stroke-width="1.5" fill="none"/></svg></div>
    <h4>Email:</h4><p>hello@vorteqlabs.example</p>
  </div>
  <div class="contact-rule" style="top:251px"></div>
  <div class="contact-item" style="top:270px">
    <div class="contact-icon"><svg width="12" height="16" viewBox="0 0 12 16"><path d="M6 0a6 6 0 0 1 6 6c0 4-6 10-6 10S0 10 0 6a6 6 0 0 1 6-6z" fill="#fff"/><circle cx="6" cy="6" r="2.2" fill="#00c6c6"/></svg></div>
    <h4>Address:</h4><p>Vorteq Studio, Harbor Lane.</p>
  </div>
  <div class="footer-divider" style="left:671px"></div>

  <h3 class="footer-heading" style="left:715px">CONTACT ME</h3>
  <div class="field" style="top:103px">Name:</div>
  <div class="field" style="top:155px">Email:</div>
  <div class="field" style="top:207px">Address:</div>
  <div class="submit">Submit Now</div>

  <div class="footer-bottom-rule"></div>
  <p class="copyright">Copyrights@2025.Vorteq Studio.All Rights Reserved</p>
</footer>

</body>
</html>
```